Stationary package for VORELO
VORELO is an outdoor and camping supplies distribution company
Professional
Yousef K Haddadin
Director
#17 Sahra Trade Gardens
Dubai
UAE
pinetrail@mailbox-ex.test
www.vorelo-supply.test

```html
<!DOCTYPE html>
<html lang="en">
<head>
<meta charset="utf-8">
<title>VORELO Business Cards</title>
<link rel="stylesheet" href="https://fonts.googleapis.com/css2?family=Archivo+Black&family=Archivo:wght@400;600;700&display=swap">
<style>
  :root {
    --stage: #1c1d1f;
    --card-white: #ffffff;
    --card-dark: #2b2b2b;
    --card-back: #3b3b3b;
    --accent-brown: #8a6a45;
    --ink-dark: #2e2e2e;
    --ink-light: #ffffff;
    --ink-muted: #d9d9d9;
  }
  * { margin: 0; padding: 0; box-sizing: border-box; }
  html, body { width: 1200px; height: 763px; overflow: hidden; background: var(--stage); }
  .canvas { position: relative; width: 1200px; height: 763px; }
  .card {
    position: absolute; width: 540px; height: 310px; overflow: hidden;
    box-shadow: 0 14px 30px rgba(0,0,0,.55);
    font-family: "Archivo", Arial, sans-serif;
  }
  .card-front { left: 40px; top: 226px; background: var(--card-white); }
  .card-back { left: 620px; top: 226px; background: var(--card-back); }
  .front-band { position: absolute; left: 0; top: 0; width: 540px; height: 310px; }
  .brand-front {
    position: absolute; left: 0; right: 0; top: 56px; text-align: center;
    font-family: "Archivo Black", Arial, sans-serif; font-size: 62px; letter-spacing: 1px;
    color: var(--ink-dark); line-height: 1;
  }
  .address {
    position: absolute; left: 0; right: 0; top: 138px; text-align: center;
    font-size: 12px; color: var(--ink-dark);
    display: flex; justify-content: center; align-items: center; gap: 6px;
  }
  .holder {
    position: absolute; left: 44px; top: 204px; color: var(--ink-light);
    font-size: 22px; font-weight: 700;
  }
  .holder .role { font-weight: 400; font-size: 17px; }
  .contacts {
    position: absolute; left: 44px; top: 244px; color: var(--ink-muted);
    font-size: 11.5px; display: flex; gap: 14px; align-items: center;
  }
  .web-line { position: absolute; left: 210px; top: 270px; color: var(--ink-muted); font-size: 11.5px; display: flex; align-items: center; gap: 6px; }
  .contact-item { display: flex; align-items: center; gap: 5px; }
  .icon { width: 11px; height: 11px; fill: var(--ink-muted); }
  .icon-dark { fill: var(--ink-dark); }
  .brand-back {
    position: absolute; left: 0; right: 0; top: 100px; text-align: center;
    font-family: "Archivo Black", Arial, sans-serif; font-size: 74px; letter-spacing: 1px;
    color: var(--ink-light); line-height: 1;
  }
  .url-back {
    position: absolute; left: 0; right: 0; top: 214px; text-align: center;
    color: var(--ink-light); font-size: 17px; font-weight: 600;
  }
</style>
</head>
<body>
<main class="canvas">
  <section class="card card-front">
    <svg class="front-band" viewBox="0 0 540 310" aria-hidden="true">
      <path d="M0 192 Q270 150 540 180 L540 310 L0 310 Z" fill="var(--card-dark)"/>
      <path d="M0 186 Q270 140 540 172 L540 178 Q270 148 0 192 Z" fill="var(--accent-brown)"/>
    </svg>
    <div class="brand-front">VORELO</div>
    <div class="address">
      <svg class="icon icon-dark" viewBox="0 0 12 12"><path d="M6 0a4 4 0 0 0-4 4c0 3 4 8 4 8s4-5 4-8a4 4 0 0 0-4-4zm0 5.5A1.5 1.5 0 1 1 6 2.5a1.5 1.5 0 0 1 0 3z"/></svg>
      <span>#17 Sahra Trade Gardens, Dubai, UAE</span>
    </div>
    <div class="holder">Yousef K Haddadin, <span class="role">Director</span></div>
    <div class="contacts">
      <span class="contact-item"><svg class="icon" viewBox="0 0 12 12"><path d="M2.5 0.5l2 2.2-1 1.3c.6 1.5 2 2.9 3.5 3.5l1.3-1 2.2 2-1.2 2.5C4.8 10.8 1.2 7.2.2 1.7z"/></svg>+971500428163</span>
      <span class="contact-item"><svg class="icon" viewBox="0 0 12 12"><rect x="3" y="0" width="6" height="12" rx="1.2"/></svg>+971500428164</span>
      <span class="contact-item"><svg class="icon" viewBox="0 0 12 12"><path d="M0 2h12v8H0z M0 2l6 4 6-4" stroke="var(--card-dark)" stroke-width=".8"/></svg>pinetrail@mailbox-ex.test</span>
    </div>
    <div class="web-line">
      <svg class="icon" viewBox="0 0 12 12"><circle cx="6" cy="6" r="5.5"/></svg>
      <span>www.vorelo-supply.test</span>
    </div>
  </section>

  <section class="card card-back">
    <div class="brand-back">VORELO</div>
    <div class="url-back">www.vorelo-supply.test</div>
  </section>
</main>
</body>
</html>
```